Can you make a cool and versatile Tarnel Ventures Powerpoint template?
See www.tarnelventures.co.uk and http://www.linkedin.com/company/tarnel-ventures-ltd/ (on the right) to see how the logos are currently used - with interchangeably white and black backgrounds.
Target Market(s)
Marketing managers, product managers in HR technology, HR consultants
Industry/Entity Type
It Company
Font styles to use
Sans Serif
Requirements
Must have
- Master slide design, fonts, color theme, etc. Ideally two variations - one with white background (using colorful logo), one with a darker background (using black/white logo).

```html
<!DOCTYPE html>
<html lang="en">
<head>
<meta charset="utf-8">
<title>Tarnel Ventures – Presentation Template</title>
<link href="https://fonts.googleapis.com/css2?family=Arimo:wght@400;700&display=swap" rel="stylesheet">
<style>
  :root {
    --ink: #111111;
    --paper: #ffffff;
    --red: #ed1c24;
    --vermilion: #f15a24;
    --amber: #fcc10f;
    --lime: #a6ce39;
    --green: #2b8a4b;
    --indigo: #2e3192;
    --plum: #8a2061;
    --magenta: #9e2a8e;
    --pink: #ff6fcf;
    --sky: #0066cc;
    --peach: #f7941d;
  }
  * { box-sizing: border-box; margin: 0; padding: 0; }
  html, body { width: 1200px; height: 1000px; overflow: hidden; background: var(--paper); }
  body { position: relative; font-family: "Arimo", Arial, sans-serif; color: var(--ink); }

  .slide { position: absolute; width: 561px; height: 354px; border: 1px solid var(--ink); background: var(--paper); }
  .slide--cover { left: 48px; top: 103px; }
  .slide--charts { left: 615px; top: 103px; }
  .slide--people { left: 48px; top: 508px; }
  .slide--stats { left: 615px; top: 508px; }

  .abs { position: absolute; }
  .title { font-weight: 700; font-size: 24px; line-height: 1; letter-spacing: -0.2px; }
  .subtitle { font-weight: 700; font-size: 14.5px; line-height: 1.2; }

  .cover-title { left: 47px; top: 216px; }
  .cover-subtitle { left: 47px; top: 241px; }
  .cover-mark { left: 285px; top: 30px; width: 210px; height: 210px; border-radius: 50%;
    background: radial-gradient(circle at 40% 35%, var(--amber), var(--red) 45%, var(--plum) 100%); opacity: .9; }

  .corner-mark { left: -1px; top: 20px; width: 34px; height: 36px; background: var(--ink); }
  .head-title { left: 35px; top: 18px; }
  .head-subtitle { left: 35px; top: 43px; }

  .social { display: flex; gap: 6px; }
  .social span { display: block; width: 12px; height: 12px; background: var(--ink); border-radius: 1px; }
  .url { font-weight: 700; font-size: 11px; }

  .brand { display: flex; flex-direction: column; gap: 6px; }
  .brand-dot { width: 14px; height: 14px; border-radius: 50%; background: var(--red); }
  .brand-name { font-size: 14px; font-weight: 400; }

  .body-text { font-weight: 700; font-size: 10.5px; line-height: 13px; }
  .caption { font-weight: 700; font-size: 8px; line-height: 10.5px; }

  .bullet { display: flex; gap: 10px; }
  .bullet::before { content: ""; flex: none; width: 9px; height: 9px; margin-top: 2px; border-radius: 50%; background: var(--green); }

  .people-group { width: 142px; height: 58px; border-radius: 20px 20px 4px 4px; }
  .people-group--indigo { background: var(--indigo); }
  .people-group--vermilion { background: var(--vermilion); }
  .people-group--green { background: var(--green); }

  svg text { font-family: "Arimo", Arial, sans-serif; font-weight: 700; fill: var(--paper); }
</style>
</head>
<body>

<!-- Cover slide -->
<section class="slide slide--cover">
  <div class="abs cover-mark" role="img" aria-label="Brand accent shape"></div>
  <h1 class="abs title cover-title">LOREM IPSUM</h1>
  <p class="abs subtitle cover-subtitle">Your Business Theme Here</p>
  <div class="abs social" style="left:431px; top:303px;"><span></span><span></span><span></span></div>
  <p class="abs url" style="left:381px; top:325px;">www.tarnelventures.co.uk</p>
</section>

<!-- Charts slide -->
<section class="slide slide--charts">
  <div class="abs corner-mark"></div>
  <h2 class="abs title head-title">LOREM IPSUM</h2>
  <p class="abs subtitle head-subtitle">Your Business Theme Here</p>

  <p class="abs body-text" style="left:40px; top:93px;">Lorem ipsum dolor<br>sit amet, consectetur<br>adipisicing elit, sed do<br>eiusmod tempor<br>incididunt ut labore<br>et dolore magna aliqua.</p>
  <p class="abs body-text" style="left:40px; top:185px;">Lorem ipsum dolor<br>sit amet, consectetur<br>adipisicing elit, sed do<br>eiusmod tempor<br>incididunt ut labore<br>et dolore magna aliqua.</p>

  <svg class="abs segment-wheel" style="left:181px; top:71px;" width="180" height="180" viewBox="-90 -90 180 180">
    <defs>
      <path id="wedge" d="M18.02,-8.68 L76.59,-36.88 A85,85 0 0 1 76.59,36.88 L18.02,8.68 A20,20 0 0 0 18.02,-8.68Z"/>
    </defs>
    <g stroke="#fff" stroke-width="4">
      <use href="#wedge" fill="var(--red)" transform="rotate(-115.7)"/>
      <use href="#wedge" fill="var(--vermilion)" transform="rotate(-64.3)"/>
      <use href="#wedge" fill="var(--amber)" transform="rotate(-12.86)"/>
      <use href="#wedge" fill="var(--lime)" transform="rotate(38.57)"/>
      <use href="#wedge" fill="var(--green)" transform="rotate(90)"/>
      <use href="#wedge" fill="var(--indigo)" transform="rotate(141.4)"/>
      <use href="#wedge" fill="var(--plum)" transform="rotate(-167.1)"/>
    </g>
    <circle r="13" fill="var(--ink)"/>
    <g font-size="10" text-anchor="middle">
      <text x="-23.9" y="-50.5">LOREM<tspan x="-23.9" dy="9">IPSUM</tspan></text>
      <text x="23.9" y="-50.5">LOREM<tspan x="23.9" dy="9">IPSUM</tspan></text>
      <text x="53.6" y="-13">LOREM<tspan x="53.6" dy="9">IPSUM</tspan></text>
      <text x="43" y="33.5">LOREM<tspan x="43" dy="9">IPSUM</tspan></text>
      <text x="0" y="54">LOREM<tspan x="0" dy="9">IPSUM</tspan></text>
      <text x="-43" y="33.5">LOREM<tspan x="-43" dy="9">IPSUM</tspan></text>
      <text x="-53.6" y="-13">LOREM<tspan x="-53.6" dy="9">IPSUM</tspan></text>
    </g>
  </svg>
  <p class="abs caption" style="left:216px; top:255px;">Lorem ipsum dolor sit amet,<br>consectetur adipisicing elit,<br>sed do eiusmod tempor.</p>

  <svg class="abs pyramid" style="left:0; top:0;" width="561" height="354" viewBox="0 0 561 354">
    <polygon points="442,69 477,138 407,138" fill="var(--indigo)"/>
    <polygon points="405,142 479,142 500.8,185 383.2,185" fill="var(--magenta)"/>
    <polygon points="381.2,189 502.8,189 529.7,242 354.3,242" fill="var(--red)"/>
    <g font-size="9" text-anchor="middle">
      <text x="442" y="120">LOREM<tspan x="442" dy="9">IPSUM</tspan></text>
      <text x="442" y="169">LOREM IPSUM</text>
      <text x="442" y="218">LOREM IPSUM</text>
    </g>
  </svg>
  <p class="abs caption" style="left:387px; top:255px;">Lorem ipsum dolor sit amet,<br>consectetur adipisicing elit,<br>sed do eiusmod tempor.</p>

  <div class="abs brand" style="left:36px; top:296px;"><span class="brand-dot"></span><span class="brand-name">Tarnel Ventures</span></div>
  <div class="abs social" style="left:424px; top:303px;"><span></span><span></span><span></span></div>
  <p class="abs url" style="left:374px; top:325px;">www.tarnelventures.co.uk</p>
</section>

<!-- Audience slide -->
<section class="slide slide--people">
  <div class="abs corner-mark"></div>
  <h2 class="abs title head-title">LOREM IPSUM</h2>
  <p class="abs subtitle head-subtitle">Your Business Theme Here</p>

  <p class="abs bullet body-text" style="left:37px; top:76px;"><span>Lorem ipsum dolor sit amet, consectetur adipisicing elit,<br>sed do eiusmod tempor incididunt ut labore et dolore magna aliqua.</span></p>
  <p class="abs bullet body-text" style="left:37px; top:116px;"><span>Lorem ipsum dolor sit amet, consectetur adipisicing elit,<br>sed do eiusmod tempor incididunt ut labore et dolore magna aliqua.</span></p>

  <div class="abs people-group people-group--indigo" style="left:39px; top:170px;" role="img" aria-label="Three person icons, indigo"></div>
  <div class="abs people-group people-group--vermilion" style="left:212px; top:170px;" role="img" aria-label="Three person icons, orange"></div>
  <div class="abs people-group people-group--green" style="left:383px; top:170px;" role="img" aria-label="Three person icons, green"></div>

  <p class="abs caption" style="left:39px; top:244px;">Lorem ipsum dolor sit amet,<br>consectetur adipisicing elit,<br>sed do eiusmod tempor.</p>
  <p class="abs caption" style="left:212px; top:244px;">Lorem ipsum dolor sit amet,<br>consectetur adipisicing elit,<br>sed do eiusmod tempor.</p>
  <p class="abs caption" style="left:384px; top:244px;">Lorem ipsum dolor sit amet,<br>consectetur adipisicing elit,<br>sed do eiusmod tempor.</p>

  <div class="abs brand" style="left:36px; top:296px;"><span class="brand-dot"></span><span class="brand-name">Tarnel Ventures</span></div>
  <div class="abs social" style="left:424px; top:303px;"><span></span><span></span><span></span></div>
  <p class="abs url" style="left:374px; top:325px;">www.tarnelventures.co.uk</p>
</section>

<!-- Statistics slide -->
<section class="slide slide--stats">
  <div class="abs corner-mark"></div>
  <h2 class="abs title head-title">LOREM IPSUM</h2>
  <p class="abs subtitle head-subtitle">Your Business Theme Here</p>

  <p class="abs bullet body-text" style="left:39px; top:76px;"><span>Lorem ipsum dolor sit amet, consectetur adipisicing elit,<br>sed do eiusmod tempor incididunt ut labore et dolore magna aliqua.ua.</span></p>

  <svg class="abs stat-pies" style="left:0; top:0;" width="561" height="354" viewBox="0 0 561 354">
    <g transform="translate(97 181)">
      <circle r="60" fill="var(--plum)"/>
      <path d="M0,0 L0,-60 A60,60 0 0 0 -30,-51.96Z" fill="var(--pink)"/>
      <text y="13" font-size="36" text-anchor="middle">96%</text>
    </g>
    <g transform="translate(283 181)">
      <circle r="60" fill="var(--indigo)"/>
      <path d="M0,0 L0,-60 A60,60 0 0 0 -56.38,-20.52Z" fill="var(--sky)"/>
      <text y="13" font-size="36" text-anchor="middle">86%</text>
    </g>
    <g transform="translate(460 181)">
      <circle r="60" fill="var(--vermilion)"/>
      <path d="M0,0 L0,-60 A60,60 0 0 0 -56.38,-20.52Z" fill="var(--peach)"/>
      <text y="13" font-size="36" text-anchor="middle">88%</text>
    </g>
  </svg>

  <p class="abs caption" style="left:37px; top:246px;">Lorem ipsum dolor sit amet,<br>consectetur adipisicing elit,<br>sed do eiusmod tempor.</p>
  <p class="abs caption" style="left:231px; top:246px;">Lorem ipsum dolor sit amet,<br>consectetur adipisicing elit,<br>sed do eiusmod tempor.</p>
  <p class="abs caption" style="left:397px; top:246px;">Lorem ipsum dolor sit amet,<br>consectetur adipisicing elit,<br>sed do eiusmod tempor.</p>

  <div class="abs brand" style="left:36px; top:296px;"><span class="brand-dot"></span><span class="brand-name">Tarnel Ventures</span></div>
  <div class="abs social" style="left:424px; top:303px;"><span></span><span></span><span></span></div>
  <p class="abs url" style="left:374px; top:325px;">www.tarnelventures.co.uk</p>
</section>

</body>
</html>
```